Pool Screen Enclosure Building a Career Boot Camp!

Looking to Host a Boot Camp for people looking for a career or looking to change careers. We Design, Manufacture and Install Custom Pool Screen Enclosures. We have a training program to allow Non Experienced motivated people the chance at a great career that will provide a great living for them and their family. This will be a paid boot camp, week long, we provide all the initial training for them to make a transition into our business. This will be 5 days of training with a guaranteed job to start the following Monday.... This is good for both someone with no construction experience or someone with construction experience that wants to upgrade their current job.
Paid Boot Camp
transition to a full time job with great pay
Benefits include Health Insurance, Dental and Vision, 401K, we provide the tools and training.

```html
<!DOCTYPE html>
<html lang="en">
<head>
<meta charset="UTF-8">
<title>Pool Screen Enclosure Career Boot Camp</title>
<link rel="stylesheet" href="https://fonts.googleapis.com/css2?family=Oswald:wght@700&family=Lato:wght@400;700;900&display=swap">
<style>
  :root{
    --stage:#545454;
    --paper:#ffffff;
    --topband:#e8e8e8;
    --ink:#111111;
    --orange:#f0962f;
    --hero-dark:#1e1e1e;
    --hero-mid:#3a3a3a;
    --white:#ffffff;
  }
  *{margin:0;padding:0;box-sizing:border-box}
  html,body{width:1200px;height:1200px;overflow:hidden;background:var(--stage)}
  .flyer{position:absolute;left:133px;top:0;width:934px;height:1200px;background:var(--paper);overflow:hidden;font-family:'Lato',sans-serif;color:var(--ink)}
  .top-band{position:absolute;left:0;top:0;width:100%;height:64px;background:var(--topband)}
  .top-band .site{position:absolute;right:36px;top:33px;font-size:13px;letter-spacing:.6px;color:var(--ink)}
  .hero{position:absolute;left:0;top:64px;width:100%;height:655px;background:linear-gradient(160deg,var(--hero-dark) 0%,var(--hero-mid) 55%,#2a2a2a 100%)}
  .headline{position:absolute;left:71px;top:150px;width:800px;font-family:'Oswald',sans-serif;font-weight:700;font-size:50px;line-height:65px;color:var(--orange);text-transform:uppercase;letter-spacing:-.3px;transform:scaleY(1.08);transform-origin:left top}
  .rule{position:absolute;left:71px;top:310px;width:737px;height:5px;background:var(--orange)}
  .tagline{position:absolute;left:82px;top:338px;font-size:19.5px;color:var(--white)}
  .photo{position:absolute;top:453px;width:288px;height:356px}
  .photo-1{left:26px;background:linear-gradient(180deg,#b9c3cc 0%,#8c949a 55%,#7a6f60 100%)}
  .photo-2{left:324px;background:linear-gradient(180deg,#6f9ad0 0%,#c8d6e6 45%,#8a7d6c 100%)}
  .photo-3{left:620px;background:linear-gradient(180deg,#9a9a90 0%,#b8a48a 55%,#a8957c 100%)}
  .intro{position:absolute;left:47px;top:820px;width:870px;font-size:17.3px;line-height:21.4px;color:var(--ink)}
  .benefits{position:absolute;left:49px;top:964px;display:flex;align-items:center;white-space:nowrap}
  .benefits h2{font-weight:900;font-size:24.5px;margin-right:26px;letter-spacing:.2px}
  .benefit{display:flex;align-items:center;font-size:17.5px;margin-right:15px}
  .benefit:last-child{margin-right:0}
  .benefit svg{width:14px;height:14px;margin-right:8px}
  .footer{position:absolute;left:0;top:1032px;width:100%;height:168px;background:linear-gradient(90deg,#e8922f 0%,#a86f32 35%,#4a3a2a 65%,#242424 100%)}
  .offer{position:absolute;left:71px;top:44px;color:var(--white)}
  .offer h3{font-weight:900;font-size:35px;line-height:38px}
  .offer p{font-size:16.8px;line-height:18px}
  .contact{position:absolute;left:601px;top:50px;color:var(--white);font-size:20px;letter-spacing:1.2px}
  .contact li{list-style:none;display:flex;align-items:center;height:28px}
  .contact svg{width:16px;height:16px;margin-right:11px}
</style>
</head>
<body>
<div class="flyer">
  <div class="top-band"><span class="site">www.companyname.com</span></div>

  <div class="hero" role="img" aria-label="Dim background photo looking up at the aluminium frame of a pool screen enclosure"></div>
  <h1 class="headline">Pool Screen Enclosure Building a<br>Career Boot Camp !</h1>
  <div class="rule"></div>
  <p class="tagline">We Design, Manufacture and Install Custom Pool Screen Enclosures.</p>

  <div class="photo photo-1" role="img" aria-label="Worker on a ladder fitting screen to an enclosure frame under a cloudy sky"></div>
  <div class="photo photo-2" role="img" aria-label="Two workers on a roof installing the top of a white screen enclosure"></div>
  <div class="photo photo-3" role="img" aria-label="Trainees crouched around construction plans on a concrete slab"></div>

  <p class="intro">We have a training program to allow Non Experienced motivated people the chance at a great career that will provide a great living for them and their family. This will be a paid boot camp, week long, we provide all the initial training for them to make a transition into our business. This will be 5 days of training with a guaranteed job to start the following Monday.... This is good for both someone with no construction experience or someone with construction experience that wants to upgrade their current job.</p>

  <div class="benefits">
    <h2>BENEFITS</h2>
    <span class="benefit"><svg viewBox="0 0 14 14"><path d="M1 8 L5 12 L13 2" fill="none" stroke="#f0962f" stroke-width="2.4" stroke-linecap="round" stroke-linejoin="round"/></svg>Health Insurance</span>
    <span class="benefit"><svg viewBox="0 0 14 14"><path d="M1 8 L5 12 L13 2" fill="none" stroke="#f0962f" stroke-width="2.4" stroke-linecap="round" stroke-linejoin="round"/></svg>Dental and Vision</span>
    <span class="benefit"><svg viewBox="0 0 14 14"><path d="M1 8 L5 12 L13 2" fill="none" stroke="#f0962f" stroke-width="2.4" stroke-linecap="round" stroke-linejoin="round"/></svg>401K</span>
    <span class="benefit"><svg viewBox="0 0 14 14"><path d="M1 8 L5 12 L13 2" fill="none" stroke="#f0962f" stroke-width="2.4" stroke-linecap="round" stroke-linejoin="round"/></svg>We provide the tools and training.</span>
  </div>

  <div class="footer" role="img" aria-label="Tinted photo of a finished pool enclosure at dusk">
    <div class="offer">
      <h3>Paid Boot Camp</h3>
      <p>transition to a full time job with great pay</p>
    </div>
    <ul class="contact">
      <li><svg viewBox="0 0 16 16"><circle cx="8" cy="8" r="7" fill="none" stroke="#fff" stroke-width="1.2"/><path d="M5.5 4.5c-.6.6-.6 2 .8 3.8s3 2.6 3.9 2.1l.7-.8-1.4-1.2-.7.5c-.6-.2-1.5-1.1-1.8-1.8l.5-.7-1.1-1.5z" fill="#fff"/></svg>123 456 78900</li>
      <li><svg viewBox="0 0 16 16"><g fill="none" stroke="#fff" stroke-width="1.1"><circle cx="8" cy="8" r="6.5"/><ellipse cx="8" cy="8" rx="3" ry="6.5"/><path d="M1.5 8h13M2.5 4.8h11M2.5 11.2h11"/></g></svg>www.companyname.com</li>
    </ul>
  </div>
</div>
</body>
</html>
```